High-end b2b furniture company needs informational/photo brochure

Please note CHANGE IN SIZE: 11 x 25.5 overall size, tri-fold brochure. Use lots of photos and must have a high-end, clean look because we are in the interior design industry. Designer must review our website to get an idea of branding! (www.halvorquist.example).

Instructions on where all photos/images should be placed are written as the file name for the jpgs/pdfs. Please ask if file name placement instructions are not clear!

There are extra images attached to use if needed, but you do not need to use all of these. There are also several images marked for the cover, but again, no need to use all of these if it looks too crowded. This will depend upon your design. (We would prefer a relatively clean, uncrowded look.)

Thank you for your hard work. I just increased the budget for first place on this project due to the large size of this brief.

Target Market(s)

Interior designers, architects, commercial property managers, shopping mall/retail managers. We sell commercial furniture ONLY (we do not sell to end consumers and we typically do not sell furniture for the home).

Industry/Entity Type

It Company

Font styles to use
Serif
Sans Serif
Other font styles liked:
• Prefer mostly sans serif, but can use serif if design calls for it. We use variations of Gil Sans MT in much of our marketing. Can use a decorative or script font for accent, but nothing that looks "old fashioned" and no cursive or anything that looks "curly."

Colors
cadf82
add136
faa54b
f78f20
ffffff

Requirements
Must have
• An upscale feel that appeals to high-end interior designers. Photography needs to be fairly large to highlight the furniture. (Text can be placed around furniture)
Nice to have
• Ample white and dark (black or charcoal gray) space
Should not have
• No old fashioned/cursive fonts. No shadows behind photos or shadows behind text boxes. Since furniture design is our business, do not cut off the lines of our furniture designs by overlapping text or images.

```html
<!DOCTYPE html>
<html lang="en">
<head>
<meta charset="utf-8">
<title>Halvorquist – Brochure Cover</title>
<link href="https://fonts.googleapis.com/css2?family=Questrial&display=swap" rel="stylesheet">
<style>
  :root {
    --page-bg: #e9e6e0;
    --paper: #f2f2f2;
    --ink: #111111;
    --ink-soft: #5a5a5a;
    --orange: #f78f20;
    --green: #add136;
  }
  html, body {
    margin: 0;
    padding: 0;
    width: 1200px;
    height: 873px;
    overflow: hidden;
    background: var(--page-bg);
    font-family: "Questrial", "Helvetica Neue", Arial, sans-serif;
  }
  .cover {
    position: absolute;
    left: 300px;
    top: 48px;
    width: 600px;
    height: 776px;
    background: var(--paper);
  }
  .photo {
    position: absolute;
  }
  .photo--lounge {
    left: 18px; top: 18px; width: 300px; height: 190px;
    background: linear-gradient(160deg, #6e4a32 0%, #a0683f 45%, #c9a27c 70%, #5a3a28 100%);
  }
  .photo--lobby {
    left: 330px; top: 18px; width: 252px; height: 250px;
    background: linear-gradient(170deg, #8a7560 0%, #c8b497 40%, #9b6e48 70%, #6b5240 100%);
  }
  .photo--gallery {
    left: 18px; top: 220px; width: 300px; height: 230px;
    background: linear-gradient(135deg, #c9453a 0%, #e2d0a8 30%, #e6e6e6 55%, #5f6c80 80%, #8a8f99 100%);
  }
  .headline {
    position: absolute;
    right: 40px;
    top: 500px;
    margin: 0;
    text-align: right;
    line-height: 1;
    text-transform: uppercase;
    font-weight: 400;
  }
  .headline__accent {
    display: block;
    color: var(--orange);
    font-size: 56px;
    letter-spacing: 2px;
  }
  .headline__line {
    display: block;
    color: var(--ink);
    font-size: 30px;
    letter-spacing: 1px;
    margin-top: 6px;
  }
  .headline__strong {
    display: block;
    color: var(--ink);
    font-size: 52px;
    letter-spacing: 2px;
    margin-top: 6px;
  }
  .brand-name {
    position: absolute;
    left: 40px;
    bottom: 48px;
    margin: 0;
    color: var(--ink-soft);
    font-size: 22px;
    letter-spacing: 3px;
    text-transform: uppercase;
  }
</style>
</head>
<body>
  <main class="cover">
    <div class="photo photo--lounge" role="img" aria-label="Photo of a commercial lounge with leather sofas, brick wall and tall windows"></div>
    <div class="photo photo--lobby" role="img" aria-label="Photo of a hotel lobby seating area with upholstered sofas and timber beams"></div>
    <div class="photo photo--gallery" role="img" aria-label="Photo of a bright waiting area with white sofa, lounge chairs and colourful wall art"></div>

    <h1 class="headline">
      <span class="headline__accent">Solve</span>
      <span class="headline__line">Your Furniture</span>
      <span class="headline__strong">Problems</span>
    </h1>

    <p class="brand-name">Halvorquist</p>
  </main>
</body>
</html>
```